Menu Board 1000mmx500mm re-design

I would like to re-design exiting menu board 1000mmx500mm. Current board letters are bit to small to read. I would like to have pictures (attached) of the food offered on it and at the same time to create balance between pictures and size of the text to be easily readable. Fonts and colours are up to designer choice but prefer warm and bright colours rather anything dark.

Target Market(s)

Food industry

Industry/Entity Type

Food

Font styles to use
Other font styles liked:
• I leave font choice to designer

Colors
FFC000
F8CF3A
FAE287
FDF2CF
FEFAEE
F0912C
F2A743
F7CA91
FBE8D2
FDF5EE
EE7325
F08F49
F5BC92
FAE3D3
FDF4ED

Requirements
Must have
• Pictures + Text
Nice to have
• Balance between images and text.
Should not have
• Can't think of any

```html
<!DOCTYPE html>
<html lang="en">
<head>
<meta charset="utf-8">
<title>Menu Board</title>
<link href="https://fonts.googleapis.com/css2?family=Kaushan+Script&family=Montserrat:wght@500;700;800&display=swap" rel="stylesheet">
<style>
  :root {
    --page: #FAE3B8;
    --board: #FDF2CF;
    --orange: #EE7325;
    --orange-mid: #F0912C;
    --amber: #F2A743;
    --dot: #FAE287;
    --ink: #111111;
    --photo-light: #F2EDE6;
    --wood: #C98A4E;
  }
  * { margin: 0; padding: 0; box-sizing: border-box; }
  html, body { width: 1200px; height: 1200px; overflow: hidden; }
  body { background: var(--page); font-family: "Montserrat", sans-serif; color: var(--ink); }

  .menu-board {
    position: absolute; left: 331px; top: 63px;
    width: 536px; height: 1073px;
    background: var(--board); overflow: hidden;
  }
  .board-header { position: absolute; left: 0; top: 0; width: 536px; height: 186px; }

  .menu-title {
    position: absolute; left: 0; top: 128px; width: 536px;
    text-align: center;
    font-family: "Kaushan Script", cursive;
    font-weight: 400; font-size: 112px; line-height: 140px;
    color: var(--orange); letter-spacing: 2px;
  }
  .hero-wrap-photo {
    position: absolute; left: 132px; top: 272px; width: 272px; height: 196px;
    border-radius: 46% 54% 50% 50% / 55% 50% 50% 45%;
    background: radial-gradient(ellipse at 55% 50%, #E9D9CB 0%, #B35A6A 45%, #7E2E44 80%);
    transform: rotate(-12deg);
  }
  .potato-photo {
    position: absolute; left: 388px; top: 402px; width: 290px; height: 275px;
    border-radius: 50%; border: 4px solid var(--orange-mid);
    background: radial-gradient(circle at 35% 45%, #F6C24A 0%, #E0962E 45%, #8C5A22 80%, #3C3A30 100%);
  }
  .veggie-wrap-photo {
    position: absolute; left: -135px; top: 748px; width: 290px; height: 270px;
    border-radius: 50%; border: 4px solid var(--orange-mid);
    background: radial-gradient(circle at 75% 50%, #F4E2B8 0%, #D9B86A 35%, #5E8A3A 65%, #B8473A 90%);
  }
  .accent-dot { position: absolute; border-radius: 50%; background: var(--dot); opacity: 0.8; }

  .menu-item { position: absolute; }
  .item-row {
    display: flex; justify-content: space-between; align-items: center;
    font-weight: 800; font-size: 24px; line-height: 28px; white-space: nowrap;
  }
  .item-name { overflow: hidden; min-width: 0; }
  .item-price { color: var(--orange); padding-left: 8px; }
  .item-desc { font-weight: 500; font-size: 12px; line-height: 14px; margin-top: 1px; }

  .column-left .menu-item { left: 34px; width: 345px; }
  .column-right .menu-item { left: 171px; width: 335px; }

  .sauces { position: absolute; left: 0; top: 946px; width: 536px; text-align: center; }
  .sauces-title {
    display: flex; justify-content: center; align-items: center; gap: 8px;
    color: var(--orange); font-weight: 800; font-size: 34px; line-height: 40px;
  }
  .sauces-title::before, .sauces-title::after {
    content: ""; width: 26px; height: 2px; background: var(--orange);
  }
  .sauces-list { font-weight: 800; font-size: 22px; line-height: 27px; margin-top: 0; }
</style>
</head>
<body>
  <main class="menu-board">
    <svg class="board-header" viewBox="0 0 536 186">
      <g role="img" aria-label="Photo of a grilled chicken wrap on a wooden board">
        <rect x="0" y="0" width="262" height="186" fill="var(--photo-light)"/>
        <ellipse cx="120" cy="100" rx="125" ry="45" fill="var(--wood)"/>
        <ellipse cx="135" cy="68" rx="90" ry="35" fill="#E6CFA8"/>
      </g>
      <g role="img" aria-label="Photo of a chicken and rocket ciabatta on a wooden board">
        <rect x="262" y="0" width="274" height="186" fill="var(--photo-light)"/>
        <ellipse cx="420" cy="120" rx="115" ry="28" fill="var(--wood)"/>
        <ellipse cx="420" cy="82" rx="80" ry="34" fill="#DDB06E"/>
      </g>
      <path d="M0,170 C40,142 100,130 170,128 C235,126 250,100 254,0 L268,0 C272,100 290,122 360,126 C440,130 500,150 536,180 L536,186 L0,186 Z"
            fill="var(--board)"/>
      <path d="M0,170 C40,142 100,130 170,128 C235,126 250,100 254,0 M268,0 C272,100 290,122 360,126 C440,130 500,150 536,180"
            fill="none" stroke="var(--orange-mid)" stroke-width="5"/>
    </svg>

    <h1 class="menu-title">Menu</h1>
    <div class="hero-wrap-photo" role="img" aria-label="Photo of a cut beetroot wrap filled with chicken and salad"></div>
    <div class="potato-photo" role="img" aria-label="Photo of golden roasted potatoes with herbs"></div>
    <div class="veggie-wrap-photo" role="img" aria-label="Photo of a toasted vegetable wrap cut in half"></div>

    <span class="accent-dot" style="left:41px;top:302px;width:15px;height:15px"></span>
    <span class="accent-dot" style="left:47px;top:435px;width:17px;height:17px"></span>
    <span class="accent-dot" style="left:461px;top:386px;width:14px;height:14px"></span>
    <span class="accent-dot" style="left:444px;top:756px;width:17px;height:17px"></span>
    <span class="accent-dot" style="left:473px;top:1006px;width:8px;height:8px"></span>

    <section class="column-left">
      <div class="menu-item" style="top:487px">
        <div class="item-row"><span class="item-name">CIABATTA.....................</span><span class="item-price">£6</span></div>
        <p class="item-desc">Roti Chicken, Rucola, Caramelized Onions,<br>Tomato, Fresh Onion</p>
      </div>
      <div class="menu-item" style="top:545px">
        <div class="item-row"><span class="item-name">WRAP.............................</span><span class="item-price">£7</span></div>
        <p class="item-desc">Roti Chicken, Crunchy Slaw, Tomato, Fresh Onions,<br>&amp; Sauce of your choice</p>
      </div>
      <div class="menu-item" style="top:609px">
        <div class="item-row"><span class="item-name">BEETROOT WRAP.......</span><span class="item-price">£8</span></div>
        <p class="item-desc">Roti Chicken, Crunchy Slaw, Tomato, Fresh Onions,<br>&amp; Sauce of your choice</p>
      </div>
      <div class="menu-item" style="top:670px">
        <div class="item-row"><span class="item-name">WATER.........................</span><span class="item-price">£1</span></div>
      </div>
    </section>

    <section class="column-right">
      <div class="menu-item" style="top:726px">
        <div class="item-row"><span class="item-name">1/4 CHICKEN BOX.......</span><span class="item-price">£9</span></div>
        <p class="item-desc">Roti Chicken,&nbsp; Veggie Rice &amp; Salad</p>
      </div>
      <div class="menu-item" style="top:783px">
        <div class="item-row"><span class="item-name">1/2 CHICKEN BOX.......</span><span class="item-price">£14</span></div>
        <p class="item-desc">Roti Chicken,&nbsp; Veggie Rice &amp; Salad</p>
      </div>
      <div class="menu-item" style="top:840px">
        <div class="item-row"><span class="item-name">ROASTED POTATOES...</span><span class="item-price">£2.5</span></div>
        <p class="item-desc">Thyme &amp; Garlic</p>
      </div>
      <div class="menu-item" style="top:897px">
        <div class="item-row"><span class="item-name">CAN &amp; JUICES...............</span><span class="item-price">£1.8</span></div>
      </div>
    </section>

    <section class="sauces">
      <h2 class="sauces-title">SAUCES</h2>
      <p class="sauces-list">SIGNATURE, BBQ, PIRI PIRI<br>SWEET CHILLI &amp; GARLIC MAYO</p>
    </section>
  </main>
</body>
</html>
```